Dental specialist needs a sharp looking letterhead

I am looking for a letterhead to be used to send letters and communication between myself (a dental specialist) and other dentists.
My office is a state of the art dental specialty office.
I need to letterhead to also state:
Gideon R. Whitfield DDS
2847 Birchmont Avenue, Suite K
West Harlow, NY 14391
(716)482-9163
fax: (716)482-9170
whitfieldroot.com (**this email address may change)

i included my logo designs.
thank you

Target Market(s)

dentists

Industry/Entity Type

Communication

Requirements
Must have
• the included logo, whether the vertical or horizontal versions

```html
<!DOCTYPE html>
<html lang="en">
<head>
<meta charset="utf-8">
<title>Keystone Endodontics P.C. Letterhead</title>
<link rel="stylesheet" href="https://fonts.googleapis.com/css2?family=Open+Sans:wght@400;700&display=swap">
<style>
  :root {
    --band-blue: #d7ebfb;
    --paper: #ffffff;
    --ink: #1c1c1c;
    --accent-blue: #4fb8f0;
    --accent-green: #8ee04a;
    --watermark: #eef6fd;
  }
  html, body {
    margin: 0;
    padding: 0;
    overflow: hidden;
    background: var(--paper);
  }
  .letterhead {
    position: relative;
    width: 852px;
    height: 1200px;
    overflow: hidden;
    background: var(--paper);
    font-family: "Open Sans", Arial, sans-serif;
    color: var(--ink);
  }
  .bands {
    position: absolute;
    inset: 0;
    width: 852px;
    height: 1200px;
  }
  .bands .band { fill: var(--band-blue); }

  .brand {
    position: absolute;
    left: 44px;
    top: 80px;
    display: flex;
    align-items: center;
    gap: 14px;
  }
  .brand-dot {
    width: 40px;
    height: 40px;
    border-radius: 50%;
    background: var(--accent-blue);
  }
  .brand-name {
    font-size: 25px;
    font-weight: 700;
    letter-spacing: 0.5px;
    color: var(--ink);
    line-height: 1;
  }

  .contact {
    position: absolute;
    right: 44px;
    top: 32px;
    text-align: right;
    font-size: 18px;
    line-height: 28px;
    color: var(--ink);
  }
  .contact p { margin: 0; }
  .contact .doctor { font-weight: 700; }

  .watermark {
    position: absolute;
    left: 0;
    right: 0;
    top: 520px;
    text-align: center;
    font-size: 92px;
    font-weight: 700;
    letter-spacing: 6px;
    color: var(--watermark);
    line-height: 1;
  }

  .tooth-art {
    position: absolute;
    left: 563px;
    top: 1047px;
    width: 192px;
    height: 108px;
    border-radius: 40px;
    background: radial-gradient(ellipse at center, rgba(142,224,74,0.45) 0%, rgba(142,224,74,0.15) 60%, rgba(142,224,74,0) 100%);
  }
</style>
</head>
<body>
  <main class="letterhead">
    <svg class="bands" viewBox="0 0 852 1200" aria-hidden="true">
      <path class="band" d="M0 0 H852 V228 C640 180 300 170 0 230 Z"/>
      <path class="band" d="M0 1119 C220 1060 480 1030 680 1040 C760 1044 820 1050 852 1056 V1200 H0 Z"/>
    </svg>

    <div class="brand">
      <span class="brand-dot"></span>
      <span class="brand-name">KEYSTONE ENDODONTICS P.C.</span>
    </div>

    <address class="contact">
      <p class="doctor">Gideon R. Whitfield DDS</p>
      <p>2847 Birchmont Avenue, Suite K</p>
      <p>West Harlow, NY 14391</p>
      <p>Phone: (716)482-9163</p>
      <p>Fax: (716)482-9170</p>
      <p>whitfieldroot.com</p>
    </address>

    <div class="watermark" aria-hidden="true">KEYSTONE</div>

    <div class="tooth-art" role="img" aria-label="Green line drawing of a tooth with dotted trails"></div>
  </main>
</body>
</html>
```